HANDYMAN SERVICES

we provide a good,and reliable service.we do all aspects of home improvement ,also all garden services,and any repairs,no job too small,free quotes .
I am aiming towards the general public for clients,also be doing special rates for the elderly,and reducing the price for anyone who does a friend reference. It will be free quotes/consultation,all work will be guaranteed.
Now the type of work we do is cctv installation,decking,patio/driveway cleaning,garages for erecting/repairs,house/garage clearances,fit alarm systems,fit or repair windows/doors,lay patios,repair roofs,decorate interior/external,erect ariaels,lay driveways,erect or repair fencing,lay drainage,repair or erect guttering and soffits,water features,erect or repair kitchens/bathrooms,also plastering,lay lawns or repair,also repair/erect sheds.
Home Improvement

```html
<!DOCTYPE html>
<html lang="en">
<head>
<meta charset="utf-8">
<title>Handyman Service Flyer</title>
<link rel="stylesheet" href="https://fonts.googleapis.com/css2?family=Gelasio:wght@700&family=Lato:wght@400&display=swap">
<style>
  :root {
    --navy: #2b3585;
    --sky: #00aeef;
    --band: rgba(33, 58, 140, 0.93);
    --page: #ffffff;
    --white: #ffffff;
  }
  * { margin: 0; padding: 0; box-sizing: border-box; }
  html, body {
    width: 1200px; height: 1000px; overflow: hidden;
    background: var(--page);
  }
  .flyer {
    position: absolute; left: 318px; top: 96px;
    width: 584px; height: 829px; overflow: hidden;
  }
  .flyer-photo {
    position: absolute; inset: 0;
    background:
      linear-gradient(90deg,
        #eceeef 0%, #e3e4e2 30%, #e9d9bf 38%, #f1e2c8 52%,
        #e7d3b2 66%, #c9b39d 72%, #5a6f97 80%, #2f4a86 90%, #3c5a96 100%);
  }
  .headline {
    position: absolute; left: 50px; top: 52px;
    font-family: "Gelasio", Georgia, serif; font-weight: 700;
    font-size: 47px; color: var(--navy); letter-spacing: 0.2px;
    white-space: nowrap;
  }
  .headline .accent { color: var(--sky); }
  .rule {
    position: absolute; left: 0; width: 100%; height: 8px;
    background: var(--sky);
  }
  .rule-top { top: 118px; }
  .rule-band-top { top: 441px; }
  .rule-band-bottom { top: 674px; height: 9px; }
  .intro {
    position: absolute; left: 50px; top: 136px; width: 340px;
    font-family: "Gelasio", Georgia, serif; font-weight: 700;
    font-size: 23.5px; line-height: 30px; color: var(--navy);
  }
  .promises {
    position: absolute; left: 50px; top: 293px; width: 300px;
    list-style: none;
    font-family: "Lato", "Gill Sans", sans-serif;
    font-size: 18.5px; line-height: 25px; color: var(--navy);
  }
  .promises li { position: relative; padding-left: 24px; }
  .promises li::before {
    content: "•"; position: absolute; left: 3px; color: var(--sky);
  }
  .services-band {
    position: absolute; left: 0; top: 449px; width: 100%; height: 225px;
    background: var(--band);
  }
  .services {
    position: absolute; top: 14px; list-style: none;
    font-family: "Lato", "Gill Sans", sans-serif;
    font-size: 13.3px; line-height: 19.5px; color: var(--white);
  }
  .services li { position: relative; padding-left: 22px; }
  .services li::before { content: "•"; position: absolute; left: 2px; }
  .services-left { left: 51px; width: 240px; }
  .services-right { left: 301px; width: 230px; }
  .call-to-action {
    position: absolute; left: 51px; top: 696px;
    font-family: "Gelasio", Georgia, serif; font-weight: 700;
    font-size: 21px; line-height: 27px; color: var(--sky);
  }
  .phone {
    position: absolute; left: 51px; top: 752px;
    font-family: "Gelasio", Georgia, serif; font-weight: 700;
    font-size: 38px; color: var(--navy); white-space: nowrap;
  }
</style>
</head>
<body>
  <main class="flyer">
    <div class="flyer-photo" role="img" aria-label="Photo of a smiling tradesman in a yellow hard hat and blue checked shirt holding a wooden plank"></div>

    <h1 class="headline">Handyman <span class="accent">Service</span></h1>
    <div class="rule rule-top"></div>

    <p class="intro">We provide a good, reliable service that covers all aspects of home improvement, garden services and any repairs.</p>

    <ul class="promises">
      <li>No job is too small</li>
      <li>Special rates for the Senior Citizens and friend referrals</li>
      <li>Free quotes and consultations</li>
      <li>All work is guaranteed</li>
    </ul>

    <div class="rule rule-band-top"></div>
    <section class="services-band">
      <ul class="services services-left">
        <li>CCTV and alarm installation</li>
        <li>Decking</li>
        <li>Patios</li>
        <li>Driveway cleaning</li>
        <li>Fitting or repairing windows and doors</li>
        <li>Garage/shed erecting and repairs</li>
        <li>Roof repairs</li>
        <li>House/garage clearances</li>
        <li>Decorating, interior and external</li>
      </ul>
      <ul class="services services-right">
        <li>Erecting aerials</li>
        <li>Laying driveways</li>
        <li>Fence erection or repair</li>
        <li>Lay drainage, repairing or erecting guttering and soffits</li>
        <li>Water features</li>
        <li>Kitchen and bathroom fitting or repairs</li>
        <li>Plastering</li>
        <li>Lawn laying</li>
      </ul>
    </section>
    <div class="rule rule-band-bottom"></div>

    <p class="call-to-action">For more information or<br>a free quote please call</p>
    <p class="phone">07700 900418</p>
  </main>
</body>
</html>
```